Orsabellitravel.com web design project + logo design

Hi,

We are a Russian online tour operator - tripwelder.com

We are looking to tranmsfer our domain to orsabellitravel.com. The website and logo need to be orsabelliesque - we are not looking to change our functionality, but we need to make the website much more attracitve to clients, much more wild looking but at the same time remaining a professional travel company.

The main concept of the website should be innovative travel (as orsabelli was an innovator). Alternatively, you could go down the artist route and go down the draw / design your own tour road.

On our website the customer is able to combine travel services (hotels, flights, Visa services, and soon chauffeur, car rental etc...) put it into their basket (the basket definitely has to look better than it is at the moment) and pay for it in one go by card.

We are also stressin our customer support with web chat, call centre etc... (call centre number at the top of the page)

We aim to provide an easy user experience, but we need to make it have some more style, so I will be waiting for what you guys can come up with.
Let me know if you have any questions - skype is: mrkolbuzov

It Company

• It is quite a simple task - to take the existing website tripwelder.com and orsabellisize it to create orsabellitravel.com, the functionality of the website will remain the same and there are not many pages in the website. Homepage, Checkout step1, Checkout step 2 (you can view both of these if you select a service) and the generic pages for T&C''s, Privacy policy etc...

IMPORTANT UPDATE

We are also looking at how the search results will look in the designs, (please do a search on our website for hotel / flight)

```html
<!DOCTYPE html>
<html lang="en">
<head>
<meta charset="utf-8">
<title>orsabellitravel</title>
<link href="https://fonts.googleapis.com/css2?family=Arimo:wght@400;700&family=Open+Sans:wght@400;600&display=swap" rel="stylesheet">
<style>
:root{
  --rust:#a9481b;
  --rust-dark:#8a3a14;
  --bark:#8b5a2b;
  --parchment-light:#f1dfb6;
  --parchment:#d9b77c;
  --parchment-dark:#b8874a;
  --skyline:#8e4f22;
  --ink:#111;
  --muted:#7d7d7d;
  --field-border:#cfcfcf;
  --field-text:#8a8a8a;
  --white:#fff;
  --tab-grey:#8c8c8c;
}
*{box-sizing:border-box;margin:0;padding:0}
html,body{width:1200px;height:900px;overflow:hidden;background:var(--white);font-family:"Arimo",Arial,sans-serif}
.page{position:relative;width:1200px;height:900px}
.header{position:absolute;left:0;top:0;width:1200px;height:218px;
  background:radial-gradient(ellipse at 50% 30%,var(--parchment-light),var(--parchment) 60%,var(--parchment-dark));}
.skyline{position:absolute;left:0;top:150px;width:1200px;height:68px;
  background:linear-gradient(180deg,rgba(142,79,34,0) 0%,rgba(142,79,34,.55) 45%,var(--skyline) 100%)}
.brand{position:absolute;left:52px;top:30px;display:flex;align-items:center;gap:16px}
.brand-mark{width:100px;height:100px;border-radius:50%;background:var(--rust)}
.brand-name{font-size:46px;font-weight:400;color:#5a4a3a;letter-spacing:-.5px}
.contact{position:absolute;right:36px;top:36px;text-align:right;color:var(--white);font-weight:700;text-shadow:0 1px 2px rgba(0,0,0,.35)}
.contact .hotline{font-size:34px;line-height:40px}
.contact .line{font-size:19px;line-height:24px}
.nav{position:absolute;right:30px;top:228px;display:flex;align-items:center;font-family:"Open Sans",Arial,sans-serif;font-size:29px;color:var(--muted)}
.nav-item{display:flex;align-items:center;gap:12px;padding:0 14px}
.nav-sep{width:6px;height:36px;background:var(--bark)}
.main-bg{position:absolute;left:0;top:277px;width:910px;height:623px;
  background:radial-gradient(ellipse at 55% 40%,#ecd3a0,#d4ac6c 60%,#b8874a)}
.search-panel{position:absolute;left:41px;top:343px;width:844px;height:442px;background:var(--white);border:3px solid #1a1a1a;border-radius:3px;box-shadow:4px 4px 12px rgba(0,0,0,.4)}
.tabs{height:40px;background:var(--rust);display:flex}
.tab{font-weight:700;font-size:17px;color:var(--white);padding:0 18px;line-height:40px}
.tab.inactive{background:var(--tab-grey);height:34px;margin-top:3px;line-height:34px}
.field-label{position:absolute;font-weight:700;font-size:17px;color:var(--ink)}
.field{position:absolute;height:36px;border:1px solid var(--field-border);border-radius:5px;font-size:17px;color:var(--field-text);padding:0 10px;line-height:36px;background:var(--white)}
.field.disabled{background:#7c7c7c;border-color:#bbb}
.select{position:absolute;height:34px;border:1px solid var(--field-border);border-radius:4px;font-size:16px;color:var(--field-text);padding-left:12px;line-height:34px}
.select .caret{position:absolute;right:3px;top:5px;width:20px;height:22px;border:1px solid #888;background:#eee}
.select .caret::after{content:"";position:absolute;left:5px;top:8px;border:5px solid transparent;border-top:6px solid #222}
.help{position:absolute;width:18px;height:18px;border-radius:50%;background:#8f8f8f;color:var(--white);font-size:13px;font-weight:700;text-align:center;line-height:18px}
.check{position:absolute;display:flex;align-items:center;gap:6px;font-size:13px;color:var(--ink)}
.check .box{width:15px;height:15px;border:1px solid #aaa;background:#f4f4f4;position:relative}
.search-btn{position:absolute;left:628px;top:347px;width:188px;height:40px;background:var(--rust);border-bottom:3px solid var(--rust-dark);color:var(--white);font-weight:700;font-size:18px;text-align:center;line-height:38px}
.sidebar-title{position:absolute;left:910px;top:310px;width:290px;text-align:center;font-family:"Open Sans",Arial,sans-serif;font-size:28px;color:var(--bark)}
.backpack{position:absolute;left:968px;top:362px;width:175px;height:235px;border-radius:40px 40px 20px 20px;background:linear-gradient(160deg,#b8895a,#8f6236)}
.side-bar{position:absolute;left:941px;width:259px;height:46px;background:var(--bark);color:var(--white);font-family:"Open Sans",Arial,sans-serif;font-size:27px;padding-left:34px;line-height:44px}
.pricing{position:absolute;left:974px;top:752px;font-family:"Open Sans",Arial,sans-serif;font-size:26px;color:var(--bark)}
</style>
</head>
<body>
<div class="page">
  <header class="header">
    <div class="skyline" role="img" aria-label="City skyline silhouette across the bottom of the header"></div>
    <div class="brand"><span class="brand-mark"></span><span class="brand-name">orsabellitravel</span></div>
    <div class="contact">
      <div class="hotline">8-800-555-0142</div>
      <div class="line">Phone: +7 (495) 010-24-68</div>
      <div class="line">(Mon-Fri) Hours: 9:00 am - 18:00</div>
    </div>
  </header>

  <nav class="nav">
    <span class="nav-item">
      <svg width="40" height="36" viewBox="0 0 40 36"><path d="M14 4h20a4 4 0 0 1 4 4v10a4 4 0 0 1-4 4h-4v6l-6-6H14a4 4 0 0 1-4-4V8a4 4 0 0 1 4-4z" fill="#a0522d"/><path d="M4 12h14a3 3 0 0 1 3 3v9a3 3 0 0 1-3 3H12l-5 6v-6H4a3 3 0 0 1-3-3v-9a3 3 0 0 1 3-3z" fill="#7a3c16"/></svg>
      FORUM
    </span>
    <span class="nav-sep"></span>
    <span class="nav-item">
      <svg width="40" height="28" viewBox="0 0 40 28"><rect width="40" height="9.3" fill="#fff" stroke="#ccc"/><rect y="9.3" width="40" height="9.4" fill="#2a4fb5"/><rect y="18.7" width="40" height="9.3" fill="#d52b1e"/></svg>
      LANGUAGE
    </span>
    <span class="nav-sep"></span>
    <span class="nav-item">
      <svg width="34" height="36" viewBox="0 0 34 36"><circle cx="17" cy="10" r="9" fill="#a0522d"/><path d="M1 36c0-10 7-15 16-15s16 5 16 15z" fill="#a0522d"/></svg>
      MY TOUR
    </span>
  </nav>

  <div class="main-bg" role="img" aria-label="Aged parchment world map background"></div>

  <section class="search-panel">
    <div class="tabs"><span class="tab">TICKETS</span><span class="tab inactive">HOTELS</span></div>

    <span class="field-label" style="left:14px;top:83px">Whence</span>
    <span class="field" style="left:135px;top:74px;width:255px">Город</span>
    <span class="field-label" style="left:419px;top:83px">Where</span>
    <span class="field" style="left:471px;top:74px;width:255px">Город</span>

    <span class="field-label" style="left:14px;top:153px">There</span>
    <span class="field" style="left:135px;top:144px;width:150px;padding-left:12px">
      <svg width="20" height="20" viewBox="0 0 20 20" style="vertical-align:-3px;margin-right:8px"><rect x="1" y="3" width="18" height="16" rx="2" fill="none" stroke="#333" stroke-width="2"/><rect x="1" y="3" width="18" height="4" fill="#333"/><g fill="#333"><rect x="4" y="9" width="3" height="3"/><rect x="9" y="9" width="3" height="3"/><rect x="14" y="9" width="3" height="3"/><rect x="4" y="14" width="3" height="3"/><rect x="9" y="14" width="3" height="3"/></g></svg>23-06-2013</span>
    <span class="field-label" style="left:379px;top:153px">Back</span>
    <span class="field disabled" style="left:471px;top:144px;width:150px"></span>
    <span class="check" style="left:631px;top:141px"><span class="box"></span>Back</span>
    <span class="check" style="left:631px;top:161px"><span class="box"><svg width="13" height="13" viewBox="0 0 13 13" style="position:absolute;left:0;top:0"><path d="M2 7l3 3 6-8" fill="none" stroke="#222" stroke-width="2"/></svg></span>One way</span>

    <span class="field-label" style="left:14px;top:224px">Passengers</span>
    <svg style="position:absolute;left:141px;top:213px" width="16" height="36" viewBox="0 0 16 36"><circle cx="8" cy="4" r="4" fill="#111"/><path d="M2 10h12v12h-3v14H5V22H2z" fill="#111"/></svg>
    <span class="select" style="left:165px;top:215px;width:58px">1<span class="caret"></span></span>
    <span class="help" style="left:247px;top:213px">?</span>
    <svg style="position:absolute;left:277px;top:220px" width="12" height="28" viewBox="0 0 12 28"><circle cx="6" cy="3" r="3" fill="#111"/><path d="M1 8h10v9H9v11H3V17H1z" fill="#111"/></svg>
    <span class="select" style="left:295px;top:215px;width:61px">0<span class="caret"></span></span>
    <span class="help" style="left:379px;top:213px">?</span>
    <svg style="position:absolute;left:407px;top:224px" width="16" height="20" viewBox="0 0 16 20"><circle cx="8" cy="3" r="3" fill="#111"/><path d="M3 8h10v6h2v3h-5v3H6v-3H1v-3h2z" fill="#111"/></svg>
    <span class="select" style="left:428px;top:215px;width:62px">0<span class="caret"></span></span>
    <span class="help" style="left:511px;top:213px">?</span>

    <span class="field-label" style="left:14px;top:294px">Class</span>
    <span class="select" style="left:135px;top:284px;width:141px">Economy<span class="caret"></span></span>

    <span class="search-btn">Search</span>
  </section>

  <aside>
    <div class="sidebar-title">BASKET</div>
    <div class="backpack" role="img" aria-label="Open canvas travel backpack used as the basket"></div>
    <div class="side-bar" style="top:620px">Empty</div>
    <div class="side-bar" style="top:687px">Payment</div>
    <div class="pricing">*pricing</div>
  </aside>
</div>
</body>
</html>
```